Single-sided business card for restaurant bellwether with new logo made on this site

Business card options with new logo including restaurant name, address, phone number and website. This business card is single-sided only and will be presented at the hostess desk for clients to take. I would like to see options based on a cream card background, a white card background, a yellow card background and a burgundy colored background. It needs to be elegant and traditional.

Target Market(s)

local and international crowd

Industry/Entity Type

restaurant

Contact Information for Business Card

address, website and phone number

Font styles to use
Serif

Colors
EE7325
F08F49
F5BC92
FAE3D3
FDF4ED

Requirements
Must have
• new logo, address, phone number, website
Should not have
• more than three colors

```html
<!DOCTYPE html>
<html lang="en">
<head>
<meta charset="utf-8">
<title>Bellwether business cards</title>
<link href="https://fonts.googleapis.com/css2?family=Marcellus&display=swap" rel="stylesheet">
<style>
  :root {
    --backdrop: #7d7d7d;
    --card: #ffffff;
    --burgundy: #3f1c18;
    --gold: #f2b42c;
    --text: #555555;
  }
  html, body {
    margin: 0;
    width: 1200px;
    height: 1002px;
    overflow: hidden;
    background: var(--backdrop);
    font-family: "Marcellus", Georgia, serif;
  }
  .business-card {
    position: absolute;
    top: 207px;
    width: 397px;
    height: 695px;
    background: var(--card);
    color: var(--text);
    text-align: center;
  }
  .business-card--burgundy { left: 144px; --accent: var(--burgundy); --rule: var(--gold); }
  .business-card--gold { left: 650px; --accent: var(--gold); --rule: var(--burgundy); }

  .brand-square {
    position: absolute;
    left: 130px;
    top: 89px;
    width: 140px;
    height: 139px;
    background: var(--accent);
  }
  .brand-name {
    position: absolute;
    left: 0;
    right: 0;
    top: 262px;
    margin: 0;
    font-size: 36px;
    font-weight: 400;
    line-height: 1;
    letter-spacing: 4px;
    padding-left: 4px;
    color: var(--burgundy);
  }
  .contact-icons {
    position: absolute;
    left: 0;
    right: 0;
    top: 411px;
    display: flex;
    justify-content: center;
    gap: 9px;
  }
  .contact-icons svg { width: 22px; height: 22px; display: block; }
  .contact-icons circle { fill: var(--accent); }

  .contact-line, .address-line {
    position: absolute;
    left: 0;
    right: 0;
    margin: 0;
    font-size: 17.5px;
    line-height: 1;
  }
  .contact-line--phone { top: 465px; }
  .contact-line--web { top: 491px; }
  .divider {
    position: absolute;
    left: 166px;
    top: 537px;
    width: 66px;
    height: 2px;
    background: var(--rule);
  }
  .address-line--1 { top: 569px; }
  .address-line--2 { top: 595px; }
  .address-line--3 { top: 621px; }
</style>
</head>
<body>

<article class="business-card business-card--burgundy">
  <div class="brand-square"></div>
  <h1 class="brand-name">BELLWETHER</h1>
  <div class="contact-icons">
    <svg viewBox="0 0 22 22" aria-label="Phone"><circle cx="11" cy="11" r="11"/><path d="M7.2 6.2c.5-.4 1.1-.3 1.4.2l1 1.6c.3.5.2 1-.2 1.3l-.6.5c.5 1.2 1.4 2.1 2.6 2.6l.5-.6c.3-.4.9-.5 1.3-.2l1.6 1c.5.3.6 1 .2 1.4l-.8.9c-.6.6-1.6.7-2.5.3-2.4-1.1-4.2-2.9-5.3-5.3-.4-.9-.3-1.9.3-2.5z" fill="#fff"/></svg>
    <svg viewBox="0 0 22 22" aria-label="Website"><circle cx="11" cy="11" r="11"/><g fill="none" stroke="#fff" stroke-width="0.9"><circle cx="11" cy="11" r="5.5"/><ellipse cx="11" cy="11" rx="2.4" ry="5.5"/><path d="M5.5 11h11M6.3 8.2h9.4M6.3 13.8h9.4"/></g></svg>
  </div>
  <p class="contact-line contact-line--phone">958-555-0142</p>
  <p class="contact-line contact-line--web">www.bellwether.com.mx</p>
  <div class="divider"></div>
  <p class="address-line address-line--1">Restaurant Bellwether</p>
  <p class="address-line address-line--2">Jacaranda 418</p>
  <p class="address-line address-line--3">Bahía Serena, Oaxaca CP 70900</p>
</article>

<article class="business-card business-card--gold">
  <div class="brand-square"></div>
  <h1 class="brand-name">BELLWETHER</h1>
  <div class="contact-icons">
    <svg viewBox="0 0 22 22" aria-label="Phone"><circle cx="11" cy="11" r="11"/><path d="M7.2 6.2c.5-.4 1.1-.3 1.4.2l1 1.6c.3.5.2 1-.2 1.3l-.6.5c.5 1.2 1.4 2.1 2.6 2.6l.5-.6c.3-.4.9-.5 1.3-.2l1.6 1c.5.3.6 1 .2 1.4l-.8.9c-.6.6-1.6.7-2.5.3-2.4-1.1-4.2-2.9-5.3-5.3-.4-.9-.3-1.9.3-2.5z" fill="#fff"/></svg>
    <svg viewBox="0 0 22 22" aria-label="Website"><circle cx="11" cy="11" r="11"/><g fill="none" stroke="#fff" stroke-width="0.9"><circle cx="11" cy="11" r="5.5"/><ellipse cx="11" cy="11" rx="2.4" ry="5.5"/><path d="M5.5 11h11M6.3 8.2h9.4M6.3 13.8h9.4"/></g></svg>
  </div>
  <p class="contact-line contact-line--phone">958-555-0142</p>
  <p class="contact-line contact-line--web">www.bellwether.com.mx</p>
  <div class="divider"></div>
  <p class="address-line address-line--1">Restaurant Bellwether</p>
  <p class="address-line address-line--2">Jacaranda 418</p>
  <p class="address-line address-line--3">Bahía Serena, Oaxaca CP 70900</p>
</article>

</body>
</html>
```